Presentation Folder for Brisk Estates

We are a new property management / real estate company in Denver Colorado and are in need of new stationary design. Attached are our business card and logo deigns. We are looking for our stationary design. We need a presentation folder design that is Professional, exciting, and approachable. We do not have a preference on folder layout (pockets, style of folding) but will most likely be using a standard two pocket folder design (roughly 9x12) but feel free to experiment with and folder style as long as we can find a place to print them. We would also like to have a matching letterhead/page design
Below is standard size of folder from lumo press
Full Bleed Size
20.87" x 16.68"
53 x 42.4 cm
6260 x 5004 pixels
Document Trim Size
20.75" x 16.56"
52.7 x 42.1 cm
6225 x 4969 pixels
Target Market(s)
We are attempting to target the top end of the real estate market in Denver Colorado. Are target market is investors in real estate.
Industry/Entity Type
Property Management
Font styles to use
Other font styles liked:
- Would like to keep font same to logo
Look and feel
Each slider illustrates characteristics of the customer's brand and the style your logo design should communicate.

```html
<!DOCTYPE html>
<html lang="en">
<head>
<meta charset="utf-8">
<title>Brisk Estates Stationery</title>
<link href="https://fonts.googleapis.com/css2?family=Ubuntu:wght@400;500;700&display=swap" rel="stylesheet">
<style>
:root{
  --blue:#4aa9cf;
  --slate:#58595b;
  --band:#5d5e60;
  --folder:#5a5b5d;
  --paper:#ffffff;
  --ink:#3f4042;
  --bg:#e8e5e1;
}
*{margin:0;padding:0;box-sizing:border-box}
html,body{width:931px;height:1200px;overflow:hidden;background:var(--bg);font-family:'Ubuntu',sans-serif;color:var(--ink)}
.stage{position:relative;width:931px;height:1200px}
.sheet{position:absolute;background:var(--paper);box-shadow:0 2px 6px rgba(0,0,0,.18)}
.band{position:absolute;left:0;right:0;bottom:0;background:var(--band);color:#fff;text-align:center;font-size:8px;letter-spacing:.5px}
.band b{color:var(--blue);font-weight:500}
.dot{position:absolute;border-radius:50%;background:#fff;border:3px solid #ddd}
.brand{font-family:'Ubuntu',sans-serif;font-weight:700;color:var(--slate);text-transform:uppercase;white-space:nowrap;line-height:1}
.tag{color:var(--slate);white-space:nowrap}
.contact{position:absolute;font-size:6.3px;line-height:8px;color:var(--ink)}
.contact .name{color:var(--blue);font-weight:700}
.ico{display:inline-block;width:4px;height:4px;border-radius:1px;background:var(--blue);margin-right:3px;vertical-align:middle}
.gap{height:5px}
/* letterhead */
.letterhead{left:44px;top:50px;width:380px;height:490px}
.letterhead .band{height:17px;line-height:17px}
/* envelope */
.envelope{left:463px;top:136px;width:424px;height:184px}
.envelope .band{height:17px;line-height:17px}
/* cards */
.card-front{left:508px;top:364px;width:157px;height:89px}
.card-front .band{height:5px;font-size:3.5px;line-height:5px}
.card-back{left:685px;top:364px;width:157px;height:89px;background:var(--folder)}
/* folder */
.folder{position:absolute;left:90px;top:570px;width:748px;height:600px}
.folder svg{position:absolute;left:0;top:0}
.folder .txt{position:absolute;color:#fff;font-size:9px;line-height:11px;letter-spacing:.6px}
</style>
</head>
<body>
<main class="stage">

  <section class="sheet letterhead" aria-label="Letterhead">
    <div class="brand" style="position:absolute;left:22px;top:44px;font-size:19px">Brisk Estates</div>
    <div class="tag" style="position:absolute;left:22px;top:65px;font-size:6.5px">Property Management and Real Estate</div>
    <div class="contact" style="left:272px;top:16px">
      <div class="name">BRISK ESTATES</div>
      <div>P.O. BOX 482210</div>
      <div>Denver, CO 80231</div>
      <div class="gap"></div>
      <div><span class="ico"></span>303 555 0148</div>
      <div><span class="ico"></span>(720) 555-0192</div>
      <div><span class="ico"></span>(720) 555-0176</div>
      <div><span class="ico"></span>dana@briskestatesCO.com</div>
    </div>
    <div class="band">www.<b>briskestates</b>CO.com</div>
    <div class="dot" style="right:2px;bottom:2px;width:24px;height:24px"></div>
  </section>

  <section class="sheet envelope" aria-label="Envelope">
    <div class="brand" style="position:absolute;left:13px;top:18px;font-size:11px">Brisk Estates</div>
    <div class="contact" style="left:13px;top:42px">
      <div class="name">BRISK ESTATES</div>
      <div>P.O. BOX 482210</div>
      <div>Denver, CO 80231</div>
      <div class="gap"></div>
      <div><span class="ico"></span>303 555 0148</div>
      <div><span class="ico"></span>(720) 555-0192</div>
      <div><span class="ico"></span>(720) 555-0176</div>
      <div><span class="ico"></span>dana@briskestatesCO.com</div>
    </div>
    <div class="band" style="text-align:left;padding-left:155px">www.<b>briskestates</b>CO.com</div>
    <div class="dot" style="right:2px;bottom:2px;width:24px;height:24px"></div>
  </section>

  <section class="sheet card-front" aria-label="Business card front">
    <div class="brand" style="position:absolute;left:9px;top:19px;font-size:7px">Brisk Estates</div>
    <div class="contact" style="left:87px;top:18px;font-size:4.5px;line-height:5.5px">
      <div class="name" style="font-size:5.5px">DANA HOLT</div>
      <div>Owner/Broker</div>
    </div>
    <div class="contact" style="left:21px;top:52px;font-size:4px;line-height:5px">
      <div class="name">BRISK ESTATES</div>
      <div>P.O. BOX 482210</div>
      <div>Denver, CO 80231</div>
    </div>
    <div class="contact" style="left:87px;top:46px;font-size:4px;line-height:5px">
      <div><span class="ico" style="width:3px;height:3px"></span>303 555 0148</div>
      <div><span class="ico" style="width:3px;height:3px"></span>(720) 555-0192</div>
      <div><span class="ico" style="width:3px;height:3px"></span>(720) 555-0176</div>
      <div><span class="ico" style="width:3px;height:3px"></span>dana@briskestatesCO.com</div>
    </div>
    <div class="band">www.<b>briskestates</b>CO.com</div>
  </section>

  <section class="sheet card-back" aria-label="Business card back">
    <div class="brand" style="position:absolute;left:0;right:0;top:52px;text-align:center;font-size:12px;color:#fff">Brisk Estates</div>
    <div class="tag" style="position:absolute;left:0;right:0;top:66px;text-align:center;font-size:5px;color:#fff">Property Management and Real Estate</div>
  </section>

  <section class="folder" aria-label="Presentation folder">
    <svg width="748" height="600" viewBox="0 0 748 600">
      <path d="M0 0 H373 V598 H50 Q30 598 30 578 V480 Q30 462 14 452 L0 444 V273 A12 12 0 0 0 0 249 Z" fill="var(--folder)"/>
      <path d="M373 0 H738 L748 10 V249 A12 12 0 0 0 748 273 V598 H396 Q380 598 378 580 L373 540 Z" fill="var(--paper)"/>
    </svg>
    <div class="txt" style="left:125px;top:211px;font-size:8px">www.<b style="color:var(--blue);font-weight:500">briskestates</b>CO.com</div>
    <div class="txt" style="left:43px;top:378px">
      <div><span class="ico"></span>303 555 0148</div>
      <div><span class="ico"></span>(720) 555-0192</div>
      <div><span class="ico"></span>(720) 555-0176</div>
      <div><span class="ico"></span>dana@briskestatesCO.com</div>
    </div>
    <div class="txt" style="left:250px;top:389px">
      <div>BRISK ESTATES</div>
      <div>P.O. BOX 482210</div>
      <div>Denver, CO 80231</div>
    </div>
    <div class="brand" style="position:absolute;left:373px;width:375px;top:244px;text-align:center;font-size:40px">Brisk Estates</div>
    <div class="tag" style="position:absolute;left:373px;width:375px;top:286px;text-align:center;font-size:14px">Property Management and Real Estate</div>
  </section>

</main>
</body>
</html>
```